Creation of an elegant and modern turnkey Shopify website

Hello,

We are a new company specializing in the sale of above-ground pools. We want to create a turnkey website, ideally using Shopify. For now, we need a "showcase" site, not an e-commerce platform, with four tabs:

Home Page (an overall presentation of the company)
Our Products (an overview of all the above-ground pools we sell)
Our Projects (a page inspired by Instagram to showcase photos of our future projects)
Contact (a page with all our contact information and a contact form)

We are looking to create a highly visual, elegant, and modern website with vibrant splashes of color. We will provide the text, photos (along with instructions on where to place them on each page), and all other necessary information as attachments.

Thank you in advance for your proposals!

The Larkmere Basin Team

Target Market(s)

Targeted at Swiss customers (a translator will need to be installed for different languages)

Industry/Entity Type

Sale of customised above-ground pools

Coding

Coded - Design and coding required

Font styles to use
Sans Serif

Colors
0094D4
00A9DD
6FCCEA
C7EBF8
E9F6FB
00AB8E
00BBA5
67D7C9
C6EFE9
E9F9F6

Requirements
Must have
• A stunning, elegant and modern look
Nice to have
• Inspiration from the colors of our logo throughout the site, but in an elegant way
Should not have
• An overly classic look for swimming pool sites

```html
<!DOCTYPE html>
<html lang="en">
<head>
<meta charset="utf-8">
<title>Larkmere Basin – Above-Ground Pools</title>
<link rel="stylesheet" href="https://fonts.googleapis.com/css2?family=Tenor+Sans&family=Poppins:wght@300;400;500&display=swap">
<style>
:root{
  --blue:#00A9DD;
  --blue-deep:#0094D4;
  --blue-soft:#6FCCEA;
  --blue-pale:#C7EBF8;
  --blue-mist:#E9F6FB;
  --graphite:#555555;
  --ink:#2b2b2b;
  --muted:#7a7a7a;
  --white:#ffffff;
  --display:"Tenor Sans", sans-serif;
  --body:"Poppins", sans-serif;
}
*{box-sizing:border-box;margin:0;padding:0}
html,body{width:1200px;height:3610px;overflow:hidden}
body{background:var(--white);font-family:var(--body);color:var(--ink);display:flex;flex-direction:column}
.wrap{width:886px;margin:0 auto}

/* header */
.site-header{height:58px;position:relative;background:var(--white);z-index:2}
.site-header .wrap{height:100%;display:flex;align-items:center;justify-content:space-between}
.nav{display:flex;gap:26px;font-size:10px;color:var(--muted)}
.nav a{color:inherit;text-decoration:none}
.nav a.active{color:var(--blue);text-decoration:underline}
.brand{position:absolute;left:50%;top:8px;transform:translateX(-50%);background:var(--white);padding:6px 14px 8px;text-align:center;font-family:var(--display);color:var(--blue);font-size:22px;line-height:1.05;letter-spacing:1px}
.header-tools{display:flex;align-items:center;gap:22px}
.lang{border:1px solid #ddd;border-radius:12px;font-size:9px;padding:4px 10px;color:var(--ink);display:flex;gap:10px}
.call{display:flex;align-items:center;gap:8px;font-size:8px;color:var(--muted)}
.call strong{display:block;font-size:10px;color:var(--ink);font-weight:500}
.call-dot{width:24px;height:24px;border-radius:50%;background:var(--blue);display:grid;place-items:center}

/* hero */
.hero{height:486px;position:relative;background:linear-gradient(160deg,#2f4a2e 0%,#1f6f86 35%,#2aa3bf 60%,#7a6a55 85%,#4c4a44 100%)}
.hero-box{position:absolute;left:50%;top:50%;transform:translate(-50%,-50%);width:366px;height:196px;background:rgba(40,62,72,.72);text-align:center;color:var(--white);padding-top:36px}
.hero-box h1{font-family:var(--display);font-weight:400;font-size:28px;line-height:1.3;letter-spacing:.5px}
.btn-light{display:inline-block;margin-top:18px;background:var(--white);color:var(--ink);font-size:10px;padding:8px 18px}
.hero-dots{position:absolute;bottom:16px;left:50%;transform:translateX(-50%);display:flex;gap:6px}
.hero-dots i{width:6px;height:6px;border-radius:50%;background:rgba(255,255,255,.5)}
.hero-dots i:first-child{background:var(--white)}

/* split rows */
.split{display:grid;gap:6px;height:362px}
.split.img-left{grid-template-columns:587px 1fr}
.split.img-right{grid-template-columns:1fr 587px}
.photo{height:100%}
.panel{padding:0 30px;display:flex;flex-direction:column;justify-content:center;font-size:9.5px;line-height:1.4}
.panel h2{font-family:var(--display);font-weight:400;font-size:20px;line-height:1.25;margin-bottom:18px}
.panel p{margin-bottom:10px}
.panel.blue{background:var(--blue);color:var(--white)}
.panel.blue h2{color:var(--white)}
.panel.blue .accent{color:var(--blue-pale)}
.panel.grey{background:var(--graphite);color:#eee}
.panel.grey h2{color:var(--blue)}
.panel .accent-title{color:var(--blue-pale)}
.warranty{font-family:var(--display);font-size:15px;color:var(--blue-pale);margin-top:6px}

.section-title{font-family:var(--display);font-weight:400;font-size:20px;text-align:center;color:#4a4a4a;padding:48px 0 24px}

/* features */
.features{display:grid;grid-template-columns:repeat(5,1fr);gap:6px}
.feature{background:var(--blue-mist);height:180px;padding:24px 12px 0}
.feature svg{width:30px;height:30px}
.feature h3{font-size:12px;font-weight:400;margin:16px 0 10px}
.feature p{font-size:8.5px;line-height:1.35;color:var(--muted)}

/* products */
.products{display:grid;grid-template-columns:repeat(4,1fr);gap:6px}
.product{background:var(--blue-mist);height:300px}
.product .photo{height:162px}
.product-body{padding:20px 18px}
.product h3{font-size:12px;font-weight:400;line-height:1.3;margin-bottom:10px}
.product p{font-size:8.5px;line-height:1.35;color:var(--muted);margin-bottom:8px}
.more{font-size:8.5px;color:var(--muted);text-decoration:underline}

.stack{margin-top:50px;display:flex;flex-direction:column;gap:6px}

/* work */
.work{display:grid;grid-template-columns:repeat(3,1fr);gap:6px}
.work-card{background:var(--blue-mist);height:250px}
.work-card .photo{height:188px}
.work-card p{padding:16px 16px 0;font-size:11px;line-height:1.3}
.pager{width:390px;height:1px;background:#ddd;margin:50px auto 0;position:relative}
.pager::after{content:"";position:absolute;left:50%;top:-1px;transform:translateX(-50%);width:50px;height:3px;background:var(--blue)}
.view-all{display:block;width:72px;margin:26px auto 0;border:1px solid #ccc;font-size:10px;text-align:center;padding:8px 0}

/* footer */
.site-footer{margin-top:60px;flex:1;background:var(--blue);color:var(--white);display:flex;align-items:center}
.site-footer .wrap{display:grid;grid-template-columns:212px 220px 160px 1fr;align-items:start}
.foot-brand{font-family:var(--display);font-size:30px;line-height:1.05;letter-spacing:1px;padding-top:30px}
.foot-col h4{font-size:11px;font-weight:500;margin-bottom:16px}
.foot-col p,.foot-col a{display:flex;gap:6px;font-size:9.5px;line-height:1.45;color:var(--white);text-decoration:none;margin-bottom:8px}
.foot-col a.active{color:var(--blue-pale)}
.map{height:104px;background:linear-gradient(135deg,#eef1f3,#dde3e8);border:4px solid var(--white)}
.bottom-bar{height:36px;background:var(--graphite);color:#eee;font-size:9px}
.bottom-bar .wrap{height:100%;display:flex;align-items:center;justify-content:space-between}
.socials{display:flex;gap:8px}
.socials i{width:14px;height:14px;border-radius:50%;background:var(--blue)}
</style>
</head>
<body>

<header class="site-header">
  <div class="wrap">
    <nav class="nav">
      <a class="active" href="#">Home</a><a href="#">Our Products</a><a href="#">Our Projects</a><a href="#">Contact Us</a>
    </nav>
    <div class="brand">LARKMERE<br>BASIN</div>
    <div class="header-tools">
      <div class="lang"><span>En</span><span>▾</span></div>
      <div class="call">
        <span class="call-dot"><svg width="12" height="12" viewBox="0 0 24 24"><path fill="#fff" d="M6.6 10.8a15 15 0 0 0 6.6 6.6l2.2-2.2c.3-.3.7-.4 1-.2 1.1.4 2.3.6 3.6.6.6 0 1 .4 1 1V20c0 .6-.4 1-1 1A17 17 0 0 1 3 4c0-.6.4-1 1-1h3.5c.6 0 1 .4 1 1 0 1.3.2 2.5.6 3.6.1.3 0 .7-.2 1z"/></svg></span>
        <span>Call Now<strong>079 000 12 34</strong></span>
      </div>
    </div>
  </div>
</header>

<section class="hero" role="img" aria-label="Curved pool with teal water, tiled deck, steel ladder, loungers and tropical plants">
  <div class="hero-box">
    <h1>We Bring Your Pool<br>Dreams To Life!</h1>
    <span class="btn-light">More Info</span>
  </div>
  <div class="hero-dots"><i></i><i></i><i></i></div>
</section>

<main>
  <section class="wrap split img-left" style="margin-top:8px">
    <div class="photo" role="img" aria-label="Lagoon-style pool among rocks and palms with a shaded lounge deck" style="background:linear-gradient(150deg,#3c5a2c,#4f9aa6 45%,#b49a74 75%,#3f4b33)"></div>
    <div class="panel blue">
      <h2>Transform Your Garden With Our Premium Above-Ground Pools!</h2>
      <p>Achieve Your Dreams With Our Custom, Tailor-Made Above-Ground Pools.</p>
      <p>Imagine An Exceptional Relaxation And Leisure Space Right In Your Own Backyard. With Our Unparalleled Expertise And Commitment To Excellence, We Create Above-Ground Pools That Exceed All Expectations. Our Exclusive, Custom-Designed Models Are Crafted To Combine Style, Durability, And Innovation, Offering A Unique And Refined Experience.</p>
    </div>
  </section>

  <h2 class="section-title">Why Choose Our Above-Ground Pools?</h2>
  <section class="wrap features">
    <div class="feature">
      <svg viewBox="0 0 32 32" fill="none" stroke="#00A9DD" stroke-width="1.5"><path d="M6 12l5-6h10l5 6-10 14z"/><path d="M6 12h20M13 6l-2 6 5 14 5-14-2-6"/></svg>
      <h3>Superior Quality:</h3>
      <p>Each Pool Is Constructed With High-Quality Materials, Ensuring Exceptional Durability And Strength.</p>
    </div>
    <div class="feature">
      <svg viewBox="0 0 32 32" fill="none" stroke="#00A9DD" stroke-width="1.5"><path d="M6 26l12-12M16 6v4M14 8h4M24 12v4M22 14h4M22 4v3M20.5 5.5h3"/></svg>
      <h3>Elegant Design:</h3>
      <p>Our Pools Come In A Variety Of Styles And Finishes, Seamlessly Blending Into Any Garden Setting.</p>
    </div>
    <div class="feature">
      <svg viewBox="0 0 32 32" fill="none" stroke="#00A9DD" stroke-width="1.5"><rect x="5" y="5" width="22" height="22"/><path d="M9 23l14-14M9 19l2 2M13 15l2 2M17 11l2 2"/></svg>
      <h3>Custom &amp; Tailor-Made:</h3>
      <p>Create The Pool Of Your Dreams With Our Customization Options, Tailored To Your Specific Tastes And Needs.</p>
    </div>
    <div class="feature">
      <svg viewBox="0 0 32 32" fill="none" stroke="#00A9DD" stroke-width="1.5"><circle cx="16" cy="16" r="5"/><path d="M16 4v4M16 24v4M4 16h4M24 16h4M7.5 7.5l3 3M21.5 21.5l3 3M7.5 24.5l3-3M21.5 10.5l3-3"/></svg>
      <h3>Easy Installation:</h3>
      <p>Enjoy Your New Oasis Quickly With Our Simple And Fast Installation Process.</p>
    </div>
    <div class="feature">
      <svg viewBox="0 0 32 32" fill="none" stroke="#00A9DD" stroke-width="1.5"><path d="M11 18a7 7 0 1 1 10 0c-1 1-1.5 2-1.5 3.5h-7c0-1.5-.5-2.5-1.5-3.5z"/><path d="M13 25h6M14 28h4M16 3V1M6 7 4.5 5.5M26 7l1.5-1.5"/></svg>
      <h3>Constant Innovation:</h3>
      <p>We Incorporate The Latest Technologies To Provide You With An Optimal And Safe Swimming Experience.</p>
    </div>
  </section>

  <h2 class="section-title">Our Products</h2>
  <section class="wrap products">
    <article class="product">
      <div class="photo" role="img" aria-label="Aluminium pool set into a stone terrace" style="background:linear-gradient(160deg,#6f7a6a,#4c7d8c 55%,#8a8178)"></div>
      <div class="product-body"><h3>Aluminium Pools</h3><p>Our Aluminium Pools Are Designed To Offer Exceptional Durability While Being Aesthetically</p><span class="more">More Info</span></div>
    </article>
    <article class="product">
      <div class="photo" role="img" aria-label="Above-ground pool with wooden cladding and steps" style="background:linear-gradient(160deg,#c9d6d8,#e8e4dc 50%,#a3784f)"></div>
      <div class="product-body"><h3>Above-Ground Pools With Aluminium And Wood</h3><p>Enhance Your Outdoor Space With Our Stylish And Durable...</p><span class="more">More Info</span></div>
    </article>
    <article class="product">
      <div class="photo" role="img" aria-label="Steel pool ladder descending into bright blue water" style="background:linear-gradient(160deg,#1a86c9,#3aa6dc 55%,#c9b79a)"></div>
      <div class="product-body"><h3>Galvanized Steel Pools With Composite Wood Coverings</h3><p>For Those Who Prefer A More Natural Look, Our Composite...</p><span class="more">More Info</span></div>
    </article>
    <article class="product">
      <div class="photo" role="img" aria-label="Round mini pool spa in a garden" style="background:linear-gradient(160deg,#6c8a5a,#5fb0c2 50%,#3c4a52)"></div>
      <div class="product-body"><h3>Mini Pool Spa</h3><p>Discover Our Mini Pool Spa, An Innovative 2-In-1 Solution That Combines</p><span class="more">More Info</span></div>
    </article>
  </section>

  <section class="wrap stack">
    <div class="split img-right">
      <div class="panel grey">
        <h2>Personalized<br>Services</h2>
        <p>We Understand That Every Garden And Client Is Unique.</p>
        <p>That's Why We Offer Personalized Services, From Design To Installation And After-Sales Support.</p>
        <p>Our Team Of Experts Is Here To Answer All Your Questions And Guide You Throughout Your Project.</p>
      </div>
      <div class="photo" role="img" aria-label="Pool cleaning hose, brush and net beside clear water" style="background:linear-gradient(150deg,#7cc7d8,#3f8fb0 50%,#b9dde6)"></div>
    </div>
    <div class="split img-left">
      <div class="photo" role="img" aria-label="Long rectangular pool with steel ladder and lush green planting" style="background:linear-gradient(150deg,#3d6b35,#2d8fc6 45%,#6cc1e6 70%,#b8a58a)"></div>
      <div class="panel blue">
        <h2 class="accent-title">Guaranteed<br>Satisfaction</h2>
        <p>Your Satisfaction Is Our Top Priority.</p>
        <p>We Are Committed To Providing You With Exceptional Service And The Highest Quality Products.</p>
        <p>Join Our Community Of Satisfied Customers Who Are Already Enjoying Their Custom Above-Ground Pools.</p>
        <div class="warranty">10-Year Warranty!</div>
      </div>
    </div>
    <div class="split img-right">
      <div class="panel grey">
        <h2>Contact Us<br>Today</h2>
        <p>Don't Wait Any Longer To Transform Your Garden Into A Wellness Oasis.</p>
        <p>Contact Us Today To Discover Our Range Of Customizable Above-Ground Pools And Get A Tailored Quote.</p>
        <p>Dive Into A World Of Infinite Possibilities With [Your Company Name].</p>
      </div>
      <div class="photo" role="img" aria-label="Person relaxing at the pool edge holding a phone, with a pink float" style="background:linear-gradient(150deg,#4fb5dc,#8fd3ea 45%,#e9e3dc 70%,#a57a55)"></div>
    </div>
  </section>

  <h2 class="section-title">Our Work</h2>
  <section class="wrap work">
    <article class="work-card">
      <div class="photo" role="img" aria-label="Hotel pool with loungers beside a modern building" style="background:linear-gradient(160deg,#cfd7da,#3f8ab1 55%,#7d6e5d)"></div>
      <p>Lorem Ipsum Is Simply Dummy Text Of The Printing Industry.</p>
    </article>
    <article class="work-card">
      <div class="photo" role="img" aria-label="Small square pool on a wooden deck with garden seating" style="background:linear-gradient(160deg,#5b6a50,#4f8d9c 55%,#8c6a4e)"></div>
      <p>Lorem Ipsum Is Simply Dummy Text Of The Printing Industry.</p>
    </article>
    <article class="work-card">
      <div class="photo" role="img" aria-label="Bright pool with orange deck chairs" style="background:linear-gradient(160deg,#3c7a4a,#3fbfd4 50%,#d98a3c)"></div>
      <p>Lorem Ipsum Is Simply Dummy Text Of The Printing Industry.</p>
    </article>
  </section>
  <div class="pager"></div>
  <span class="view-all">View All</span>
</main>

<footer class="site-footer">
  <div class="wrap">
    <div class="foot-brand">LARKMERE<br>BASIN</div>
    <div class="foot-col">
      <h4>Contact Us</h4>
      <p>☏ 079 000 12 34</p>
      <p>✉ info@larkmerebasin.com</p>
      <p><span>⌖</span><span>Elio Marchetti<br>Rue des Vergers 27<br>1860 Aigle</span></p>
    </div>
    <div class="foot-col">
      <h4>Quick Links</h4>
      <a class="active" href="#">Home</a><a href="#">Our Products</a><a href="#">Our Projects</a><a href="#">Contact Us</a>
    </div>
    <div class="map" role="img" aria-label="Street map showing the showroom location"></div>
  </div>
</footer>
<div class="bottom-bar">
  <div class="wrap">
    <span>© 2024 The Larkmere Basin. All Right Reserved</span>
    <div class="socials"><i></i><i></i><i></i></div>
  </div>
</div>

</body>
</html>
```